Hotel Business Card Project

Amber Crest Hotel will be a premium boutique hotel in Dhaka, Bangladesh. The hotel will offer the finest amenities and facilities available on the market, and the cost per room investment will far exceed other 5-star hotels currently in the market.

As a result, we wanted the business card to reflect that premium/luxurious/upscale feel, and also be elegant and hospitable at the same time.

The name 'Amber Crest' is derived from the fact that Bangladesh has 6 distinct seasons (you can get more information online if required, or contact me about it). The leaves in the logo has the tree because trees give people shade, protection and safety (just like our hotel would try to give).

Target Market(s)

Business professionals, guests

Industry/Entity Type

Investment

Requirements
Must have
• Elegant, Classy and very attractive business card.

Must be editable to enter specific Names, Positions, Phone numbers and email later on.
Nice to have
• The address would be: House 42, Road 57, Banani 4, Dhaka 1230, Bangladesh

Slogan- Luxury Redefined

```html
<!DOCTYPE html>
<html lang="en">
<head>
<meta charset="utf-8">
<title>Amber Crest Hotel — Business Card</title>
<link rel="stylesheet" href="https://fonts.googleapis.com/css2?family=Arimo:wght@400;700&family=Jost:wght@400;500&display=swap">
<style>
  :root {
    --backdrop: #7d7d7d;
    --card-teal: #148ea6;
    --card-white: #fbfbfb;
    --ink-teal: #1a8ba3;
    --ink-dark: #1c1c1c;
    --ink-grey: #6e6e6e;
    --leaf-amber: #d98a2b;
    --on-teal: #eaf6f8;
  }
  * { box-sizing: border-box; margin: 0; padding: 0; }
  html, body { width: 1200px; height: 900px; overflow: hidden; }
  body {
    background: var(--backdrop);
    display: flex;
    flex-direction: column;
    align-items: center;
    justify-content: center;
    gap: 40px;
  }
  .card {
    width: 665px;
    height: 380px;
    border-radius: 22px;
    position: relative;
    overflow: hidden;
    box-shadow: 0 8px 24px rgba(0,0,0,.25);
  }

  /* Back side */
  .card-back { background: var(--card-teal); }
  .card-back .brand {
    position: absolute;
    top: 120px;
    right: 70px;
    display: flex;
    align-items: center;
    gap: 14px;
  }
  .card-back .brand-dot {
    flex: none;
    width: 22px; height: 22px; border-radius: 50%;
    background: var(--leaf-amber);
  }
  .card-back .brand-name {
    font-family: "Jost", sans-serif;
    font-weight: 500;
    font-size: 40px;
    letter-spacing: 2px;
    color: var(--on-teal);
    text-transform: uppercase;
    white-space: nowrap;
  }
  .card-back .web {
    position: absolute;
    left: 40px;
    bottom: 34px;
    font-family: "Arimo", sans-serif;
    font-weight: 700;
    font-size: 17px;
    letter-spacing: 1px;
    color: var(--on-teal);
  }

  /* Front side */
  .card-front { background: var(--card-white); display: flex; }
  .card-front .logo-panel {
    width: 50%;
    padding: 90px 20px 0 30px;
    display: flex;
    align-items: center;
    justify-content: center;
    gap: 10px;
  }
  .card-front .brand-dot {
    flex: none;
    width: 16px; height: 16px; border-radius: 50%;
    background: var(--leaf-amber);
  }
  .card-front .brand-name {
    font-family: "Jost", sans-serif;
    font-weight: 500;
    font-size: 22px;
    letter-spacing: 1px;
    color: var(--ink-grey);
    text-transform: uppercase;
    white-space: nowrap;
  }
  .card-front .contact-panel {
    width: 50%;
    padding: 110px 30px 0 20px;
  }
  .person-name {
    font-family: "Arimo", sans-serif;
    font-weight: 700;
    font-size: 22px;
    color: var(--ink-teal);
  }
  .person-role {
    font-family: "Arimo", sans-serif;
    font-size: 14px;
    color: var(--ink-dark);
    margin-top: 2px;
    margin-left: 8px;
  }
  .address {
    display: flex;
    gap: 10px;
    margin-top: 28px;
    margin-left: 8px;
    font-family: "Jost", sans-serif;
    font-size: 16px;
    line-height: 1.3;
    color: var(--ink-grey);
  }
  .address svg { flex: none; margin-top: 3px; }
</style>
</head>
<body>
  <section class="card card-back">
    <div class="brand">
      <span class="brand-dot"></span>
      <span class="brand-name">Amber Crest</span>
    </div>
    <p class="web">www.ambercresthotel.com</p>
  </section>

  <section class="card card-front">
    <div class="logo-panel">
      <span class="brand-dot"></span>
      <span class="brand-name">Amber Crest Hotel</span>
    </div>
    <div class="contact-panel">
      <h1 class="person-name">Rafiq Hossain</h1>
      <p class="person-role">Manager</p>
      <div class="address">
        <svg width="12" height="16" viewBox="0 0 12 16" aria-hidden="true">
          <path d="M6 0a6 6 0 0 0-6 6c0 4.5 6 10 6 10s6-5.5 6-10a6 6 0 0 0-6-6zm0 8.5A2.5 2.5 0 1 1 6 3.5a2.5 2.5 0 0 1 0 5z" fill="var(--ink-teal)"/>
        </svg>
        <p>House 42, Road 57, Banani 4,<br>Dhaka 1230, Bangladesh</p>
      </div>
    </div>
  </section>
</body>
</html>
```